menu for prepared meals company

Currently have a menu set up with company logo, would like something more eye catching and artistic to make it look professional. This is a fitness and health driven company in regards to purchasing prepared meals to use towards fitness goals. Do not necessarily want the menu to be geared towards muscular men and women. Looking to have the menu be simple to understand, exactly what it stands for, and geared towards a large demographic in health and life style eating changes.

Target Market(s)

health/fitness

Industry/Entity Type

It Company

Requirements
Must have
• *please see set up for mock menu and apply changes that were applied in the word document menu information.
• ex:do not offer sweet potato and chicken hash*

```html
<!DOCTYPE html>
<html lang="en">
<head>
<meta charset="utf-8">
<title>Fresh Fuel Meals – The Menu</title>
<link rel="stylesheet" href="https://fonts.googleapis.com/css2?family=Fjalla+One&family=Crimson+Pro:wght@400;700&family=Yellowtail&display=swap">
<style>
  :root{
    --page:#ffffff;
    --side-top:#ee3a3a;
    --side-bottom:#431116;
    --side-top-soft:#d4504e;
    --side-bottom-soft:#441318;
    --paper:#f6e7bf;
    --paper-light:#fbf0d4;
    --brush:#f3b83a;
    --brush-dark:#e9a52a;
    --bar:#f2a94a;
    --box:#f7c677;
    --box-light:#f8d28e;
    --ink:#3a2414;
    --head:#2a1a0c;
    --bell:#d0762c;
    --logo-red:#e3262e;
  }
  *{box-sizing:border-box;margin:0;padding:0}
  html,body{width:900px;height:1200px;overflow:hidden;background:var(--page)}
  .canvas{position:relative;width:900px;height:1200px}
  .menu{position:absolute;left:40px;width:820px;height:575px;background:linear-gradient(135deg,var(--paper) 0%,var(--paper-light) 55%,var(--paper) 100%);font-family:"Crimson Pro",serif;color:var(--ink)}
  .menu--first{top:18px}
  .menu--second{top:605px}
  .sidebar{position:absolute;left:0;top:0;width:187px;height:100%;background:linear-gradient(180deg,var(--side-top) 0%,var(--side-top) 30%,var(--side-bottom) 100%)}
  .menu--second .sidebar{background:linear-gradient(180deg,var(--side-top-soft) 0%,var(--side-top-soft) 30%,var(--side-bottom-soft) 100%)}
  .sidebar__motif{position:absolute;left:50px;width:86px;background:rgba(120,20,25,.28);border-radius:6px}
  .sidebar__motif--top{top:0;height:172px}
  .sidebar__motif--bottom{top:325px;height:250px}
  .brand{position:absolute;left:36px;top:188px;width:116px;height:116px;border-radius:50%;background:#fff;border:5px solid #c7252b;display:flex;align-items:center;justify-content:center;text-align:center;font-family:"Fjalla One",sans-serif;font-size:17px;line-height:1.1;color:var(--logo-red)}
  .title{position:absolute;left:40px;top:420px;font-family:"Yellowtail",cursive;font-size:46px;color:#fff;line-height:1}
  .title small{position:absolute;left:56px;top:-12px;font-family:"Fjalla One",sans-serif;font-size:14px;letter-spacing:2px;color:var(--side-top)}
  .col{position:absolute;top:0;width:172px}
  .col--specials{left:213px}
  .col--build1{left:406px}
  .col--build2{left:596px}
  .bell{position:absolute;top:12px;left:138px;width:18px;height:14px}
  .heading{position:absolute;top:30px;left:-4px;width:180px;height:28px;background:linear-gradient(90deg,var(--brush-dark),var(--brush) 20%,var(--brush) 85%,rgba(243,184,58,.6));border-radius:3px 8px 4px 10px;font-family:"Fjalla One",sans-serif;font-size:15px;color:var(--head);padding:4px 14px;display:flex;justify-content:space-between}
  .dish{position:absolute;left:0;width:170px}
  .dish__name{background:var(--bar);font-weight:700;font-size:9px;padding:6px 14px;height:22px}
  .dish__desc{background:var(--box-light);font-size:9px;line-height:1.15;padding:8px 14px}
  .table{position:absolute;left:0;width:168px;font-size:9px}
  .table--main{top:66px;height:140px;background:var(--box)}
  .table--fish{top:206px;height:114px;background:var(--box-light)}
  .table--carb{top:66px;height:120px;background:var(--box)}
  .table--vege{top:216px;height:140px;background:var(--box)}
  .row{display:flex;align-items:center;height:19.5px;padding-left:16px}
  .row--head{height:34px;font-weight:700;align-items:center;line-height:1.05}
  .row--note{font-weight:700;height:24px;margin-top:4px}
  .row span:first-child{width:68px}
  .row span{width:46px;text-align:center}
  .row--fish span:first-child{width:94px}
  .notes{position:absolute;top:370px;left:0;width:172px;font-size:8.6px;line-height:1.12}
  .notes p{margin-bottom:6px;padding-left:6px;text-indent:-6px}
</style>
</head>
<body>
<div class="canvas">

  <section class="menu menu--first">
    <div class="sidebar">
      <div class="sidebar__motif sidebar__motif--top" role="img" aria-label="Faint barbell silhouette motif"></div>
      <div class="sidebar__motif sidebar__motif--bottom" role="img" aria-label="Faint fork silhouette motif"></div>
      <div class="brand">Fresh Fuel<br>Meals</div>
      <div class="title"><small>THE</small>Menu</div>
    </div>

    <div class="col col--specials">
      <div class="heading"><span>Specialty Meals</span><span>$9.95</span></div>
      <div class="dish" style="top:68px"><div class="dish__name">Pasta with Turkey Meatballs</div><div class="dish__desc">Whole Grain Pasta<br>with Turkey Meatballs &amp; Tomato Sauce</div></div>
      <div class="dish" style="top:146px"><div class="dish__name">Stir Fry</div><div class="dish__desc">Chicken, Stir Fry Vegetable Mix<br>with Jasmine Rice</div></div>
      <div class="dish" style="top:226px"><div class="dish__name">Turkey Burger</div><div class="dish__desc">Turkey Patty on a Multigram Flat Bread<br>with side of sweet potato fries</div></div>
      <div class="dish" style="top:306px"><div class="dish__name">Stuffed Pepper</div><div class="dish__desc">Pepper stuffed with Ground Turkey<br>Your Choice of Whole Grain or<br>Jasmine Rice Combined in a Red Sauce</div></div>
    </div>

    <div class="col col--build1">
      <svg class="bell" viewBox="0 0 18 14"><circle cx="9" cy="2" r="1.5" fill="var(--bell)"/><path d="M2 11a7 7 0 0 1 14 0z" fill="var(--bell)"/><rect x="0" y="11.5" width="18" height="2" fill="var(--bell)"/></svg>
      <div class="heading"><span>Create Your Own &nbsp;- &nbsp;Part 1</span></div>
      <div class="table table--main">
        <div class="row row--head"><span>Choose Protein</span><span>Half Size<br>(4 Oz)</span><span>Full Size<br>(8 Oz)</span></div>
        <div class="row"><span>Chicken</span><span>$7.95</span><span>$8.95</span></div>
        <div class="row"><span>Ground Beef</span><span>$7.95</span><span>$8.95</span></div>
        <div class="row"><span>Ground Turkey</span><span>$7.95</span><span>$8.95</span></div>
        <div class="row"><span>Steak</span><span>$9.95</span><span>$10.95</span></div>
        <div class="row"><span>Turkey Tenderloin</span><span>$7.95</span><span>$8.95</span></div>
      </div>
      <div class="table table--fish">
        <div class="row row--note">All Fish Portions are 6 Oz</div>
        <div class="row row--fish"><span>Salmon</span><span>$11.95</span></div>
        <div class="row row--fish"><span>Tilapia</span><span>$10.95</span></div>
        <div class="row row--fish"><span>Cod</span><span>$9.95</span></div>
        <div class="row row--fish"><span>Veggie Burger</span><span>$9.95</span></div>
      </div>
    </div>

    <div class="col col--build2">
      <svg class="bell" viewBox="0 0 18 14"><circle cx="9" cy="2" r="1.5" fill="var(--bell)"/><path d="M2 11a7 7 0 0 1 14 0z" fill="var(--bell)"/><rect x="0" y="11.5" width="18" height="2" fill="var(--bell)"/></svg>
      <div class="heading"><span>Create Your Own &nbsp;- &nbsp;Part 2</span></div>
      <div class="table table--carb">
        <div class="row row--head"><span>Carb Choices</span><span>Half Size<br>(1/2 Cup)</span><span>Full Size<br>(1 Cup)</span></div>
        <div class="row"><span>Whole Grain Pasta</span><span>$</span><span>$</span></div>
        <div class="row"><span>Whole Grain Rice</span><span>$</span><span>$</span></div>
        <div class="row"><span>Jasmine Rice</span><span>$</span><span>$</span></div>
        <div class="row"><span>Sweet Potato</span><span>$</span><span>$</span></div>
      </div>
      <div class="table table--vege">
        <div class="row row--head"><span>Vege Choices</span><span>Half Size<br>(1/2 Cup)</span><span>Full Size<br>(1 Cup)</span></div>
        <div class="row"><span>Green Beans</span><span>$</span><span>$</span></div>
        <div class="row"><span>Broccoli</span><span>$</span><span>$</span></div>
        <div class="row"><span>Spinach</span><span>$</span><span>$</span></div>
        <div class="row"><span>Asparagus</span><span>$</span><span>$</span></div>
      </div>
      <div class="notes">
        <p>* If two vegetable options are wanted they may choose two for low carb meal combo.</p>
        <p>* Also offer gluten free pasta as a carb option.</p>
        <p>* Offer at home or delivery within 20 miles for small fee.</p>
      </div>
    </div>
  </section>

  <section class="menu menu--second">
    <div class="sidebar">
      <div class="sidebar__motif sidebar__motif--top" role="img" aria-label="Faint barbell silhouette motif"></div>
      <div class="sidebar__motif sidebar__motif--bottom" role="img" aria-label="Faint fork silhouette motif"></div>
      <div class="brand">Fresh Fuel<br>Meals</div>
      <div class="title"><small>THE</small>Menu</div>
    </div>

    <div class="col col--specials">
      <div class="heading"><span>Specialty Meals</span><span>$9.95</span></div>
      <div class="dish" style="top:68px"><div class="dish__name">Pasta with Turkey Meatballs</div><div class="dish__desc">Whole Grain Pasta<br>with Turkey Meatballs &amp; Tomato Sauce</div></div>
      <div class="dish" style="top:146px"><div class="dish__name">Stir Fry</div><div class="dish__desc">Chicken, Stir Fry Vegetable Mix<br>with Jasmine Rice</div></div>
      <div class="dish" style="top:226px"><div class="dish__name">Turkey Burger</div><div class="dish__desc">Turkey Patty on a Multigram Flat Bread<br>with side of sweet potato fries</div></div>
      <div class="dish" style="top:306px"><div class="dish__name">Stuffed Pepper</div><div class="dish__desc">Pepper stuffed with Ground Turkey<br>Your Choice of Whole Grain or<br>Jasmine Rice Combined in a Red Sauce</div></div>
    </div>

    <div class="col col--build1">
      <svg class="bell" viewBox="0 0 18 14"><circle cx="9" cy="2" r="1.5" fill="var(--bell)"/><path d="M2 11a7 7 0 0 1 14 0z" fill="var(--bell)"/><rect x="0" y="11.5" width="18" height="2" fill="var(--bell)"/></svg>
      <div class="heading"><span>Create Your Own &nbsp;- &nbsp;Part 1</span></div>
      <div class="table table--main">
        <div class="row row--head"><span>Choose Protein</span><span>Half Size<br>(4 Oz)</span><span>Full Size<br>(8 Oz)</span></div>
        <div class="row"><span>Chicken</span><span>$7.95</span><span>$8.95</span></div>
        <div class="row"><span>Ground Beef</span><span>$7.95</span><span>$8.95</span></div>
        <div class="row"><span>Ground Turkey</span><span>$7.95</span><span>$8.95</span></div>
        <div class="row"><span>Steak</span><span>$9.95</span><span>$10.95</span></div>
        <div class="row"><span>Turkey Tenderloin</span><span>$7.95</span><span>$8.95</span></div>
      </div>
      <div class="table table--fish">
        <div class="row row--note">All Fish Portions are 6 Oz</div>
        <div class="row row--fish"><span>Salmon</span><span>$11.95</span></div>
        <div class="row row--fish"><span>Tilapia</span><span>$10.95</span></div>
        <div class="row row--fish"><span>Cod</span><span>$9.95</span></div>
        <div class="row row--fish"><span>Veggie Burger</span><span>$9.95</span></div>
      </div>
    </div>

    <div class="col col--build2">
      <svg class="bell" viewBox="0 0 18 14"><circle cx="9" cy="2" r="1.5" fill="var(--bell)"/><path d="M2 11a7 7 0 0 1 14 0z" fill="var(--bell)"/><rect x="0" y="11.5" width="18" height="2" fill="var(--bell)"/></svg>
      <div class="heading"><span>Create Your Own &nbsp;- &nbsp;Part 2</span></div>
      <div class="table table--carb">
        <div class="row row--head"><span>Carb Choices</span><span>Half Size<br>(1/2 Cup)</span><span>Full Size<br>(1 Cup)</span></div>
        <div class="row"><span>Whole Grain Pasta</span><span>$</span><span>$</span></div>
        <div class="row"><span>Whole Grain Rice</span><span>$</span><span>$</span></div>
        <div class="row"><span>Jasmine Rice</span><span>$</span><span>$</span></div>
        <div class="row"><span>Sweet Potato</span><span>$</span><span>$</span></div>
      </div>
      <div class="table table--vege">
        <div class="row row--head"><span>Vege Choices</span><span>Half Size<br>(1/2 Cup)</span><span>Full Size<br>(1 Cup)</span></div>
        <div class="row"><span>Green Beans</span><span>$</span><span>$</span></div>
        <div class="row"><span>Broccoli</span><span>$</span><span>$</span></div>
        <div class="row"><span>Spinach</span><span>$</span><span>$</span></div>
        <div class="row"><span>Asparagus</span><span>$</span><span>$</span></div>
      </div>
      <div class="notes">
        <p>* If two vegetable options are wanted they may choose two for low carb meal combo.</p>
        <p>* Also offer gluten free pasta as a carb option.</p>
        <p>* Offer at home or delivery within 20 miles for small fee.</p>
      </div>
    </div>
  </section>

</div>
</body>
</html>
```